Commercial Auto Insurance Application and Commercial Property Insurance Application

Hi I need a fillable application for my business to send to potential clients for Commercial Auto Insurance and Commercial Property Insurance. I have attached an example application I currently use for another line of insurance.
Commercial Auto Insurance Application
On the first page I would need the following:
- Business Name: (fill in area for text)
- Effective Date: (fill in area for text)
- How do you structure your business? (Check box for “Sole Proprietor”, “Partnership”, “Corporation”, “LLC”)
- Contact Name: (fill in area for text) / Phone Number: (fill in area for text) / Contact Email (fill in area for text)
- Mailing address: (fill in area for text)
- Garaging location: (fill in area for text)
- Owner Name: (fill in area for text)
- Description of Operations: (fill in area for text)
- How long has the operation been in business? (fill in area for text)
- How many years of experience does your management have in the truck/transportation industry? (fill in area for text)
Coverages
Liability Combined Single Limit: ($1,000,000 (checkbox) / $500,000 (checkbox / $300,000 (checkbox) / Other: (fill in area for text)
Uninsured Motorist CSL: (fill in area for text) (checkbox for “Rejected”)
Medical Payments: (fill in area for text)
Physical Damage: (fill in area for text) (checkbox for Rejected)
Liability Deducible: ($500 checkbox, $1,000 checkbox, $2,500 checkbox, $5,000 checkbox)
Physical Damage Deductible: ($500 checkbox, $1,000 checkbox, $2,500 checkbox, $5,000 checkbox)
Driving radius: (fill in area for text)
How many years have you had your own continuous commercial auto insurance coverage for the current business name? (fill in area for text)
Do any of your vehicles travel across state lines? Yes (checkbox)/ No (checkbox)
If yes, please list all states in which vehicles operate: (fill in area for text)
What is the maximum radius traveled for your customer's business?
0-25 miles (checkbox)
26-50 miles (checkbox)
51-75 miles (checkbox)
76-100 miles (checkbox)
101-150 miles (checkbox)
151-200 miles (checkbox)
201-300 miles (checkbox)
300+ miles (checkbox)
Would you like physical damage coverage for this vehicle? (should be for each vehicle listed)
On the 2nd page of the application I would need the following:
I would need to have it where people can fill in the vehicle information such as VIN:, Year:, Make:, Model:, Type of Vehicle:, Trailers:, Value:
I would also need to have it where people can fill in the drivers with their driver info including Name:, DOB:, DL #:, DL State:, Class of License:, Married: Yes/No, Number of years driving similar vehicle:
Please make it where you can fill in 20 vehicle's information and 20 driver's info.
For the 2nd Application I would need one for Property Insurance
On the Commercial Property Application I would need the following:
- Building Address: (fill in area for text)
- Building Description: (fill in area for text)
- Building Amount: $(fill in area for text)
- Business Personal Property Amount: $ (fill in area for text) (checkbox for Not Needed)
- Building Sq Ft: (fill in area for text)
- Total Area Sq Ft: (fill in area for text)
- Building Construction Type: Wood Frame (checkbox), Steel (checkbox), Fire Resistive (checkbox), Non-Combustible (checkbox), Other (fill in area for text)
- # of stories: (fill in area for text)
- Year Built: (fill in area for text)
- Wiring improvement year: (fill in area for text)
- Roofing improvement year: (fill in area for text)
- Plumbing improvement year: (fill in area for text)
- Heating improvement year: (fill in area for text)
- What is to the right of the building and distance: (fill in area for text)
- What is to the left of the building and distance: (fill in area for text)
- What is in front of the building and distance: (fill in area for text)
- What is behind the building and distance: (fill in area for text)
- Burglar alarm installation and serviced by: (fill in area for text) None (checkbox)
- Does the premises have fire protection? Sprinkler system (checkbox), Fire detection (checkbox), Other: (fill in area for text) None (checkbox)

```html
<!DOCTYPE html>
<html lang="en">
<head>
<meta charset="utf-8">
<title>Commercial Auto Insurance Application</title>
<link href="https://fonts.googleapis.com/css2?family=Arimo:wght@400;700&display=swap" rel="stylesheet">
<style>
  :root{
    --navy:#253a7d;
    --green:#0e9b48;
    --teal:#17706a;
    --ink:#2a2a2e;
    --rule:#b9b9bf;
    --shade:#f0ebeb;
    --box:#ececec;
    --box-edge:#cfcfcf;
    --box-on:#9a9a9a;
    --backdrop:#a9a9a9;
    --paper:#ffffff;
  }
  *{box-sizing:border-box;margin:0;padding:0}
  html,body{width:1200px;height:1200px;overflow:hidden}
  body{background:var(--backdrop);font-family:"Arimo",Arial,sans-serif;color:var(--ink)}
  .application{
    position:absolute;left:195px;top:26px;width:1052px;height:1489px;
    background:var(--paper);transform:scale(.77);transform-origin:0 0;
  }
  .brand{position:absolute;left:30px;top:52px;display:flex;align-items:center;gap:12px}
  .brand-mark{width:22px;height:22px;background:var(--green)}
  .brand-name{font-size:27px;font-weight:700;color:var(--navy);letter-spacing:.5px;line-height:1.15}
  .office{position:absolute;right:30px;top:22px;text-align:right;font-size:21px;line-height:24.6px}
  .block{position:absolute;left:27px;width:997px;border:2px solid var(--rule);border-top-width:1px}
  .row{display:grid;border-top:1px solid var(--rule);font-size:21px}
  .row:first-child{border-top:none}
  .cell{display:flex;align-items:center;padding-left:14px;white-space:nowrap}
  .cell.shaded{background:var(--shade)}
  .cell.split{border-left:1px solid var(--rule)}
  .options{display:flex;align-items:center}
  .option{display:flex;align-items:center;gap:12px;position:absolute}
  .check{display:inline-block;width:15px;height:15px;background:var(--box);border:1px solid var(--box-edge);flex:none}
  .check.on{background:var(--box-on);border-color:var(--box-on)}
  .band{
    position:absolute;left:27px;width:997px;height:55px;
    background:linear-gradient(90deg,var(--navy) 0%,var(--teal) 50%,var(--green) 100%);
    color:#fff;font-weight:700;font-size:21px;display:flex;align-items:center;padding-left:14px;
  }
  .band-body{position:absolute;left:27px;width:997px;height:55px;border:2px solid var(--rule);border-top:none}
  .rel{position:relative}
  .multi{flex-direction:column;align-items:flex-start;justify-content:center;line-height:30px}
  .inline-checks{display:flex;align-items:center;gap:8px;flex-wrap:wrap}
  .inline-checks .check{margin-left:4px}
</style>
</head>
<body>
<main class="application">
  <header>
    <div class="brand"><span class="brand-mark"></span><span class="brand-name">PRAIRIEVIEW<br>INSURANCE SERVICES</span></div>
    <address class="office" style="font-style:normal">Prairieview Insurance Services<br>2480 Meridian Ave Suite 310<br>Lakeview, CA 91870<br>Tel: (555) 201-4478</address>
  </header>

  <section class="block" style="top:134px">
    <div class="row" style="height:53px;grid-template-columns:185px 311px 187px 1fr">
      <div class="cell">Business Name:</div><div class="cell shaded"></div>
      <div class="cell split">Effective Date:</div><div class="cell shaded"></div>
    </div>
    <div class="row rel" style="height:58px;grid-template-columns:378px 1fr">
      <div class="cell">How do you structure your business?</div>
      <div class="cell split rel">
        <span class="option" style="left:14px"><i class="check"></i>Sole Proprietor</span>
        <span class="option" style="left:208px"><i class="check"></i>Partnership</span>
        <span class="option" style="left:370px"><i class="check"></i>Corporation</span>
        <span class="option" style="left:528px"><i class="check"></i>LLC</span>
      </div>
    </div>
    <div class="row" style="height:53px;grid-template-columns:378px 182px 1fr">
      <div class="cell">Contact Name:</div><div class="cell shaded">Mailing address:</div><div class="cell"></div>
    </div>
    <div class="row" style="height:56px;grid-template-columns:510px 155px 1fr">
      <div class="cell">Garaging location:</div><div class="cell shaded split">Owner Name</div><div class="cell"></div>
    </div>
  </section>

  <h2 class="band" style="top:376px">Description of Operations:</h2>
  <div class="band-body" style="top:431px"></div>

  <section class="block" style="top:508px">
    <div class="row" style="height:53px;grid-template-columns:493px 1fr">
      <div class="cell">How long has the operation been in business?</div><div class="cell shaded"></div>
    </div>
    <div class="row" style="height:59px;grid-template-columns:1fr">
      <div class="cell">How many years of experience does your management have in the truck/transportation industry?</div>
    </div>
    <div class="row" style="height:51px;grid-template-columns:1fr"><div class="cell shaded"></div></div>
  </section>

  <h2 class="band" style="top:697px">Coverages</h2>
  <section class="block" style="top:751px;border-top:none">
    <div class="row" style="height:57px;grid-template-columns:378px 1fr">
      <div class="cell">Liability Combined Single Limit:</div>
      <div class="cell split rel">
        <span class="option" style="left:14px"><i class="check"></i>$1,000,000</span>
        <span class="option" style="left:208px"><i class="check"></i>$500,000</span>
        <span class="option" style="left:370px"><i class="check"></i>$300,000</span>
      </div>
    </div>
    <div class="row" style="height:52px;grid-template-columns:378px 258px 1fr">
      <div class="cell">Other:</div><div class="cell shaded">Uninsured Motorist CSL:</div><div class="cell"></div>
    </div>
    <div class="row" style="height:56px;grid-template-columns:121px 389px 213px 1fr">
      <div class="cell shaded" style="gap:10px"><i class="check on"></i>Other:</div><div class="cell"></div>
      <div class="cell split">Medical Payments:</div><div class="cell shaded"></div>
    </div>
    <div class="row" style="height:54px;grid-template-columns:509px 146px 1fr">
      <div class="cell" style="padding-left:18px">Physical Damage:</div>
      <div class="cell shaded" style="gap:10px;padding-left:18px"><i class="check on"></i>Rejected</div><div class="cell"></div>
    </div>
    <div class="row" style="height:54px;grid-template-columns:274px 1fr">
      <div class="cell shaded" style="padding-left:18px">Liability Deducible:</div>
      <div class="cell rel">
        <span class="option" style="left:17px"><i class="check"></i>$500</span>
        <span class="option" style="left:199px"><i class="check"></i>$1,000</span>
        <span class="option" style="left:405px"><i class="check"></i>$2,500</span>
        <span class="option" style="left:611px"><i class="check"></i>$5,000</span>
      </div>
    </div>
    <div class="row" style="height:54px;grid-template-columns:308px 1fr">
      <div class="cell shaded" style="padding-left:18px">Physical Damage Deductible:</div>
      <div class="cell rel">
        <span class="option" style="left:16px"><i class="check"></i>$500</span>
        <span class="option" style="left:165px"><i class="check"></i>$1,000</span>
        <span class="option" style="left:371px"><i class="check"></i>$2,500</span>
        <span class="option" style="left:577px"><i class="check"></i>$5,000</span>
      </div>
    </div>
  </section>

  <section class="block" style="top:1102px">
    <div class="row" style="height:46px;grid-template-columns:163px 1fr">
      <div class="cell" style="padding-left:18px">Driving radius:</div><div class="cell shaded"></div>
    </div>
    <div class="row" style="height:75px;grid-template-columns:1fr">
      <div class="cell multi" style="padding-left:18px"><span>How many years have you had your own continuous commercial auto insurance coverage</span><span>for the current business name?</span></div>
    </div>
    <div class="row" style="height:47px;grid-template-columns:492px 1fr">
      <div class="cell shaded" style="padding-left:18px">Do any of your vehicles travel across state lines?</div>
      <div class="cell inline-checks" style="padding-left:14px"><i class="check"></i> Yes/ <i class="check"></i>No</div>
    </div>
    <div class="row" style="height:42px;grid-template-columns:516px 1fr">
      <div class="cell" style="padding-left:16px">If yes, please list all states in which vehicles operate:</div><div class="cell shaded"></div>
    </div>
    <div class="row" style="height:80px;grid-template-columns:1fr">
      <div class="cell multi" style="padding-left:16px;line-height:33px">
        <span class="inline-checks">What is the maximum radius traveled for your customer's business? <i class="check"></i>0-25 miles <i class="check"></i>26-50 miles</span>
        <span class="inline-checks"><i class="check" style="margin-left:0"></i>51-75 miles <i class="check"></i>76-100 <i class="check"></i>101-150 miles <i class="check"></i>151-200 miles <i class="check"></i>201-300 miles <i class="check"></i>300+ miles</span>
      </div>
    </div>
    <div class="row" style="height:42px;grid-template-columns:1fr;border-top:none">
      <div class="cell shaded" style="padding-left:16px">Would you like physical damage coverage for this vehicle? (should be for each vehicle listed)</div>
    </div>
    <div class="row" style="height:26px;grid-template-columns:1fr;border-top:none"><div class="cell"></div></div>
  </section>
</main>
</body>
</html>
```